Business Card Design for a Personal Trainer

I need a business card design for my job as a personal trainer. It should have a unique, modern and exclusive design. On the front there should be only my logo with my name and my job. 0163/2918374 Tobias Kellinger Lindenfeldweg 14 80412 Munich Germany The most important contact information is the web adress. it can be bigger than the rest, but its not necessary. The card should be 8,5cmx5,5cm big. Font: Roboto. Colors: black, white, gray, 56c1ff.

```html
<!DOCTYPE html>
<html lang="de">
<head>
<meta charset="utf-8">
<title>Tobias Kellinger – Personal Trainer Visitenkarte</title>
<link href="https://fonts.googleapis.com/css2?family=Roboto:wght@300;400;500;700&display=swap" rel="stylesheet">
<style>
  :root {
    --page-bg: #f1f1f1;
    --card-dark: #2a2a2a;
    --card-light: #ffffff;
    --ink: #1c1c1c;
    --ink-light: #ffffff;
    --watermark: #eeeeee;
    --photo-top: #4a4a4a;
    --photo-bottom: #1f1f1f;
    --rule: #d9d9d9;
  }
  * { margin: 0; padding: 0; box-sizing: border-box; }
  html, body {
    width: 1136px; height: 1200px; overflow: hidden;
    background: var(--page-bg);
    font-family: "Roboto", sans-serif;
  }
  .card {
    position: absolute;
    top: 437px;
    width: 520px; height: 326px;
    box-shadow: 0 4px 10px rgba(0,0,0,0.35);
    overflow: hidden;
  }
  /* Back side: contacts + portrait */
  .card--back { left: 28px; background: var(--card-light); }
  .card--back .watermark {
    position: absolute; left: 36px; top: 46px;
    font-size: 38px; font-weight: 700; letter-spacing: 2px;
    color: var(--watermark);
  }
  .card--back .portrait {
    position: absolute; right: 0; top: 0;
    width: 231px; height: 100%;
    background: var(--card-dark);
  }
  .card--back .portrait .photo {
    position: absolute; left: 28px; right: 28px; top: 30px; bottom: 0;
    background: linear-gradient(180deg, var(--photo-top), var(--photo-bottom));
    border-radius: 70px 70px 0 0;
  }
  .contacts {
    position: absolute; left: 22px; top: 150px;
    width: 262px;
    list-style: none;
    color: var(--ink);
    font-size: 15px; font-weight: 500; letter-spacing: 0.8px;
  }
  .contacts li {
    display: flex; align-items: flex-start;
    margin-bottom: 11px; line-height: 18px;
    white-space: nowrap;
  }
  .contacts svg { width: 13px; height: 13px; margin: 3px 9px 0 0; flex: none; fill: var(--ink); }
  /* Front side: name */
  .card--front {
    left: 588px; background: var(--card-dark); color: var(--ink-light);
    display: flex; flex-direction: column; align-items: center;
  }
  .brand {
    margin-top: 70px;
    display: flex; align-items: center; gap: 14px;
    font-size: 34px; font-weight: 500; letter-spacing: 3px;
  }
  .brand .mark { width: 22px; height: 22px; background: var(--ink-light); }
  .name {
    margin-top: 44px;
    font-size: 31px; font-weight: 400; letter-spacing: 0.5px;
    text-transform: uppercase;
  }
  .role {
    margin-top: 4px;
    display: flex; align-items: center; gap: 8px;
    font-size: 13px; font-weight: 400; letter-spacing: 3.5px;
    text-transform: uppercase;
  }
  .role::before, .role::after {
    content: ""; width: 48px; height: 1px; background: var(--rule);
  }
</style>
</head>
<body>
  <section class="card card--back">
    <div class="watermark">KELLINGER</div>
    <ul class="contacts">
      <li><svg viewBox="0 0 24 24"><path d="M6.6 10.8a15 15 0 0 0 6.6 6.6l2.2-2.2a1 1 0 0 1 1-.25 11.4 11.4 0 0 0 3.6.6 1 1 0 0 1 1 1V20a1 1 0 0 1-1 1A17 17 0 0 1 3 4a1 1 0 0 1 1-1h3.5a1 1 0 0 1 1 1c0 1.25.2 2.450.6 3.6a1 1 0 0 1-.25 1z"/></svg>0163/2918374</li>
      <li><svg viewBox="0 0 24 24"><path d="M2 5h20v14H2zm2 2v.5l8 5 8-5V7zm0 2.8V17h16V9.8l-8 5z"/></svg>t.kellinger@trainpost.de</li>
      <li><svg viewBox="0 0 24 24"><path d="M12 2a10 10 0 1 0 0 20 10 10 0 0 0 0-20zm6.9 6h-3a15 15 0 0 0-1.3-3.9A8 8 0 0 1 18.9 8zM12 4c.8 1.2 1.5 2.5 1.9 4h-3.8c.4-1.5 1.1-2.8 1.9-4zM4.3 14a8 8 0 0 1 0-4h3.4a16 16 0 0 0 0 4zm.8 2h3a15 15 0 0 0 1.3 3.9A8 8 0 0 1 5.1 16zm3-8h-3a8 8 0 0 1 4.3-3.9A15 15 0 0 0 8.1 8zM12 20c-.8-1.2-1.5-2.5-1.9-4h3.8c-.4 1.5-1.1 2.8-1.9 4zm2.3-6H9.7a14 14 0 0 1 0-4h4.6a14 14 0 0 1 0 4zm.3 5.9a15 15 0 0 0 1.3-3.9h3a8 8 0 0 1-4.3 3.9zM16.3 14a16 16 0 0 0 0-4h3.4a8 8 0 0 1 0 4z"/></svg>www.tobiaskellinger.de</li>
      <li><svg viewBox="0 0 24 24"><path d="M12 2a7 7 0 0 0-7 7c0 5.3 7 13 7 13s7-7.7 7-13a7 7 0 0 0-7-7zm0 9.5a2.5 2.5 0 1 1 0-5 2.5 2.5 0 0 1 0 5z"/></svg><span>Lindenfeldweg 14<br>80412 München</span></li>
    </ul>
    <div class="portrait">
      <div class="photo" role="img" aria-label="Black and white portrait of the trainer, arms crossed, in a fitted long-sleeve sports shirt"></div>
    </div>
  </section>

  <section class="card card--front">
    <div class="brand"><span class="mark"></span>KELLINGER</div>
    <div class="name">Tobias Kellinger</div>
    <div class="role">Personal Trainer</div>
  </section>
</body>
</html>
```